Need a Hollin & Co
* logo
* word and powerpoint livery
* basic webpage

Hollin & Co is a Private M&A Advisor. We want to look like http://www.vantrelcapital.example
It needs to communicate reliabity, conservativeness and discretion.

```html
<!DOCTYPE html>
<html lang="en">
<head>
<meta charset="utf-8">
<title>Hollin &amp; Co — Private M&amp;A Advisor</title>
<link href="https://fonts.googleapis.com/css2?family=Michroma&family=Lato:wght@400;700&family=Open+Sans:wght@400&display=swap" rel="stylesheet">
<style>
:root{
  --green:#77b545;
  --ink:#3a3a3a;
  --text:#5e5e5e;
  --muted:#7a7a7a;
  --rule:#e2e2e2;
  --nav-bg:#f4f4f4;
  --nav-active:#b3b3b3;
  --footer:#3f3f3f;
  --footer-base:#333333;
  --footer-text:#bdbdbd;
  --white:#ffffff;
}
*{margin:0;padding:0;box-sizing:border-box}
html,body{width:931px;height:1200px;overflow:hidden;background:var(--white)}
body{position:relative;font-family:"Lato",sans-serif;font-weight:400;color:var(--text)}
.abs{position:absolute}
.display{font-family:"Michroma",sans-serif;font-weight:400}
h2,h3{font-weight:400}

.brand{left:102px;top:26px;font-size:21px;color:var(--ink);letter-spacing:1.5px}
.nav{left:349px;top:24px;width:481px;height:34px;background:var(--nav-bg);display:flex;align-items:center;font-family:"Open Sans",sans-serif;font-size:9.6px;color:#555;text-transform:uppercase}
.nav a{color:inherit;text-decoration:none;padding:0 7.8px;line-height:34px}
.nav a.active{background:var(--nav-active);color:var(--white);width:60px;text-align:center;padding:0}
.nav .search{position:absolute;left:450px;top:5px;width:24px;height:24px;background:var(--green)}

.hero{left:101px;top:82px;width:729px;height:296px;background:linear-gradient(180deg,#ede4d3 0%,#d8b98a 35%,#8a5a3a 70%,#4b3a33 100%)}
.hero-caption{left:186px;top:201px;width:492px;height:103px;background:rgba(60,60,60,.55)}
.hero-title{left:203px;top:211px;font-size:13.8px;color:var(--white)}
.hero-lede{left:202px;top:255px;width:470px;font-size:13.6px;line-height:21px;color:var(--white)}
.arrow{top:222px;width:28px;height:28px}

.card-img{top:428px;height:122px}
.card-title{top:574px;font-size:15px;color:var(--ink);text-align:center}
.card-text{top:604px;width:196px;font-size:10.5px;line-height:17px;text-align:center;color:var(--text)}
.card-text em{color:var(--green)}

.divider{left:101px;top:691px;width:729px;height:1px;background:var(--rule)}

.section-head{font-size:15px;color:var(--ink)}
.section-head span{color:var(--green)}
.about-copy{left:102px;width:466px;font-size:10.4px;line-height:18.5px}
.btn{left:102px;top:885px;width:87px;height:30px;background:var(--green);color:var(--white);font-size:11.5px;font-weight:700;line-height:30px;text-align:center}
.vrule{left:585px;top:728px;width:1px;height:204px;background:var(--rule)}

.news{left:601px;width:212px;height:64px}
.news .day{position:absolute;left:0;width:62px;top:0;text-align:center;font-size:16px;font-weight:700;color:#666;border-bottom:1px solid var(--rule);line-height:24px}
.news .mon{position:absolute;left:0;width:62px;top:26px;text-align:center;font-size:10.5px;color:#666}
.news .blurb{position:absolute;left:69px;top:2px;width:145px;font-size:10.4px;line-height:17px}
.news-sep{left:601px;width:212px;height:1px;background:var(--rule)}

.footer{left:0;top:983px;width:931px;height:173px;background:var(--footer)}
.footer-base{left:0;top:1156px;width:931px;height:44px;background:var(--footer-base)}
.f-head{font-size:12px;color:#eee;letter-spacing:.3px}
.f-list{list-style:none;font-size:10.4px;color:var(--footer-text);line-height:18px}
.social{left:298px;top:1032px;list-style:none}
.social li{display:flex;align-items:center;height:28px;font-size:10.4px;color:var(--footer-text)}
.social i{width:20px;height:20px;border-radius:50%;background:#d9d9d9;margin-right:14px;display:inline-block}
.map{left:447px;top:1010px;width:171px;height:107px;background:linear-gradient(135deg,#e6e3d7 0%,#cfd8c2 45%,#f1c26a 70%,#a8c8d8 100%)}
.loc{left:646px;font-size:10.4px;line-height:18.5px;color:var(--footer-text)}
.copyright{left:0;width:877px;top:1172px;text-align:center;font-size:10.4px;color:var(--footer-text)}
</style>
</head>
<body>

<div class="abs brand display">Hollin &amp; Co</div>
<nav class="abs nav">
  <a class="active" href="#">Home</a>
  <a href="#" style="padding-left:14px">About us</a>
  <a href="#">Services</a>
  <a href="#">Gallery</a>
  <a href="#">Blog</a>
  <a href="#">Testimonials</a>
  <a href="#">Contact us</a>
  <span class="search"><svg width="24" height="24" viewBox="0 0 24 24"><circle cx="11" cy="11" r="3.6" fill="none" stroke="#fff" stroke-width="1.6"/><line x1="13.6" y1="13.6" x2="16" y2="16" stroke="#fff" stroke-width="1.8"/></svg></span>
</nav>

<div class="abs hero" role="img" aria-label="Sunlit city skyline of high-rise office towers"></div>
<div class="abs hero-caption"></div>
<div class="abs hero-title display">WE ARE A PRIVATE M&amp;A ADVISOR</div>
<p class="abs hero-lede">We are a small investment bank. We buy/sell medium to large businesses and help them raise finance. We provide advice to them.</p>
<svg class="abs arrow" style="left:102px" viewBox="0 0 28 28"><polyline points="17,7 10,14 17,21" fill="none" stroke="#fff" stroke-width="2"/></svg>
<svg class="abs arrow" style="left:801px" viewBox="0 0 28 28"><polyline points="11,7 18,14 11,21" fill="none" stroke="#fff" stroke-width="2"/></svg>

<div class="abs card-img" style="left:101px;width:221px;background:linear-gradient(135deg,#5fae3c,#8cc65a)" role="img" aria-label="Key illustration with padlock pattern on green"></div>
<div class="abs card-img" style="left:354px;width:222px;background:linear-gradient(180deg,#f4f4f4,#cfc8bf);border:1px solid #ddd" role="img" aria-label="Stacked balanced stones"></div>
<div class="abs card-img" style="left:608px;width:219px;background:linear-gradient(135deg,#2f3c55,#7d8aa0 60%,#b7b9bd)" role="img" aria-label="Team joining hands together"></div>

<div class="abs card-title display" style="left:101px;width:221px">Secretive</div>
<div class="abs card-title display" style="left:354px;width:222px">Solid</div>
<div class="abs card-title display" style="left:608px;width:219px">Reliable</div>

<p class="abs card-text" style="left:113px">Neque porro quisquam est qui dolorem ipsum quia dolor sit amet, consectetur, adipisci velit. <em>More &gt;&gt;</em></p>
<p class="abs card-text" style="left:367px">Neque porro quisquam est qui dolorem ipsum quia dolor sit amet, consectetur, adipisci velit. <em>More &gt;&gt;</em></p>
<p class="abs card-text" style="left:619px">Neque porro quisquam est qui dolorem ipsum quia dolor sit amet, consectetur, adipisci velit. <em>More &gt;&gt;</em></p>

<div class="abs divider"></div>

<h2 class="abs section-head display" style="left:104px;top:722px">About <span>Us</span></h2>
<p class="abs about-copy" style="top:757px">Lorem ipsum dolor sit amet, consectetur adipiscing elit, sed do eiusmod tempor incididunt ut labore et dolore magna aliqua. Ut enim ad minim veniam, quis nostrud exercitation ullamco laboris nisi ut aliquip ex ea commodo consequat.</p>
<p class="abs about-copy" style="top:833px">Lorem ipsum dolor sit amet, consectetur adipiscing elit, sed do eiusmod tempor incididunt ut labore et dolore magna aliqua. Ut enim ad minim veniam, quis nostrud.</p>
<a class="abs btn">Learn More</a>

<div class="abs vrule"></div>

<h2 class="abs section-head display" style="left:601px;top:723px">Latest <span>News</span></h2>
<div class="abs news" style="top:758px"><span class="day">02</span><span class="mon">Aug 2014</span><p class="blurb">Neque porro quisquam est qui dolorem ipsum quia dolor.</p></div>
<div class="abs news-sep" style="top:814px"></div>
<div class="abs news" style="top:821px"><span class="day">04</span><span class="mon">Aug 2014</span><p class="blurb">Neque porro quisquam est qui dolorem ipsum quia dolor.</p></div>
<div class="abs news-sep" style="top:875px"></div>
<div class="abs news" style="top:885px"><span class="day">06</span><span class="mon">Aug 2014</span><p class="blurb">Neque porro quisquam est qui dolorem ipsum quia dolor.</p></div>

<footer>
  <div class="abs footer"></div>
  <div class="abs footer-base"></div>

  <h3 class="abs f-head" style="left:105px;top:1006px">NAVIGATION LINK</h3>
  <ul class="abs f-list" style="left:104px;top:1033px">
    <li>Home</li><li>Solutions</li><li>Services</li><li>Partners</li><li>Clients</li><li>About Us</li>
  </ul>

  <h3 class="abs f-head" style="left:300px;top:1008px">FOLLOW US</h3>
  <ul class="abs social">
    <li><i></i>Circlebook</li>
    <li><i></i>Chirper</li>
    <li><i></i>Orbitly</li>
    <li><i></i>RSS</li>
  </ul>

  <div class="abs map" role="img" aria-label="Street map showing the office location"></div>

  <h3 class="abs f-head" style="left:646px;top:1012px">LOCATION</h3>
  <p class="abs loc" style="top:1035px">222, Street Number, Buliding Number,<br>Area Name, City Name, Zip Code.</p>
  <p class="abs loc" style="top:1082px">Call Us : 587 240 1193<br>Email : info@hollinco.example</p>

  <p class="abs copyright">©2014 Hollin &amp; Co - Terms of Service - Privacy Policy</p>
</footer>

</body>
</html>
```